Zerovan Medical

We are a medical supplier company we sell machines and equipment to all medical sectors in Iraq. Our services include not only the installation of these machines and equipment but also we provide support after installation and we train the staff to use these machines/equipment
We need a website that will make us stand out from our competitors, something professional and catchy
Starting from the home page, before showing the home page we want the loading screen to have our logo animated in a nice way
Then we can proceed to creating the other pages which are
Projects
Services
Training
About
and Contact us
Attached below is our logo and the color blue that we hope to use in the theme of the website
**** In the home page we want to focus on our partners and services****

Target Market(s)

Medical Sector

Industry/Entity Type

Medical

Coding

Coded - Design and coding required

Number of Pages Required

5+ page

Colors
0054AA
0677BA
7BADD7
CADEEF
E8F1F8

Requirements
Must have
• Animation in loading screen or animation in home page
Nice to have
• Some sort of animation for our partners

```html
<!DOCTYPE html>
<html lang="en">
<head>
<meta charset="utf-8">
<title>Zerovan Medical</title>
<link href="https://fonts.googleapis.com/css2?family=Poppins:wght@400;500;600;700&family=Raleway:wght@600;700&display=swap" rel="stylesheet">
<style>
:root{
  --navy:#1f1f5c;
  --blue:#1a9ad8;
  --sky:#3aa8dd;
  --teal:#2b8db3;
  --pale:#e8f1f8;
  --ink:#111;
  --gray:#777;
  --white:#fff;
}
*{margin:0;padding:0;box-sizing:border-box}
html,body{width:1200px;height:3755px;overflow:hidden;background:var(--white);font-family:'Poppins',sans-serif;color:var(--ink)}
.page{position:relative;width:1200px;height:3755px;overflow:hidden}
.abs{position:absolute}
.brand-name{font-family:'Poppins',sans-serif;font-weight:700;color:var(--navy)}
.header .brand{left:90px;top:26px;display:flex;align-items:center;gap:12px}
.header .brand .mark{width:36px;height:36px;background:var(--blue)}
.header .brand .brand-name{font-size:30px}
.contact-chip{display:flex;align-items:center;gap:16px;top:22px}
.contact-chip .ico{width:54px;height:54px;border-radius:50%;background:var(--blue);display:flex;align-items:center;justify-content:center}
.contact-chip b{display:block;font-size:15px;font-weight:600;color:var(--navy)}
.contact-chip span{font-size:12px;color:#444}
.nav{left:0;top:92px;width:1200px;height:53px;background:var(--navy)}
.nav a{position:absolute;top:17px;color:#fff;font-size:16px;text-decoration:none}
.nav .cta{top:13px;left:882px;width:99px;height:27px;background:var(--blue);font-size:12px;text-align:center;line-height:27px}
.nav .soc{position:absolute;top:15px;width:22px;height:22px;display:flex;align-items:center;justify-content:center}
.hero-img{left:590px;top:165px;width:610px;height:520px;background:radial-gradient(ellipse 50% 48% at 55% 50%,rgba(236,241,245,.95),rgba(196,210,220,.75) 45%,rgba(70,110,140,.35) 75%,rgba(255,255,255,0) 100%)}
.hero h1{left:77px;top:282px;font-family:'Raleway',sans-serif;font-size:46px;line-height:54px;color:#fff;font-weight:700}
.hero p{left:75px;top:408px;width:490px;font-size:12px;line-height:15px;color:#fff}
.btn{position:absolute;font-size:17px;color:#fff;text-align:center}
.about-img{left:75px;top:938px;width:384px;height:384px;border-radius:50%;background:radial-gradient(circle at 55% 45%,#f3f7fb,#c9dbea 45%,#8fb1cf 85%,#6f97bd)}
.about h2{left:560px;top:985px;font-size:46px;font-weight:600}
.about p{left:558px;top:1070px;width:572px;font-size:15px;line-height:23.5px;color:var(--gray)}
.services{left:0;top:1433px;width:1200px;height:616px;background:radial-gradient(ellipse at 75% 20%,rgba(255,255,255,.18),rgba(255,255,255,0) 45%),linear-gradient(180deg,#44b2e3,#2a9fd6 60%,#3aa6da)}
.svc-img{width:272px;height:272px;border-radius:50%;top:1628px}
.svc-label{top:1925px;width:360px;text-align:center;font-size:30px;font-weight:500;color:#fff}
.partner{top:2177px;width:247px;height:68px;background:#fff;border-radius:6px;box-shadow:0 6px 18px rgba(0,0,0,.1);display:flex;align-items:center;justify-content:center;gap:12px;font-size:28px;font-weight:600;color:var(--navy)}
.partner i{width:18px;height:18px;background:var(--blue);display:block}
.projects h2{left:0;width:1200px;top:2358px;text-align:center;font-size:46px;font-weight:600}
.proj{top:2479px;width:274px;height:430px;border-radius:137px;background:#fff;box-shadow:0 10px 30px rgba(0,0,0,.1)}
.proj.active{background:var(--blue)}
.proj .pic{position:absolute;left:30px;top:31px;width:214px;height:214px;border-radius:50%}
.proj p{position:absolute;left:28px;top:290px;width:218px;text-align:center;font-size:12.5px;line-height:18px;color:#333}
.proj.active p{color:#fff}
.proj .go{position:absolute;left:105px;top:398px;width:64px;height:64px;border-radius:50%;background:var(--navy);display:flex;align-items:center;justify-content:center}
.footer-band{left:0;top:3278px;width:1200px;height:477px;background:var(--navy)}
.contact-box{left:118px;top:3050px;width:967px;height:330px;background:#fff;box-shadow:0 6px 24px rgba(0,0,0,.08)}
.contact-box h3{position:absolute;left:0;width:477px;top:42px;text-align:center;font-size:27px;font-weight:600}
.field{position:absolute;height:22px;background:#e9e9e9;font-size:6px;color:#999;padding:6px 7px}
.send{position:absolute;left:79px;top:267px;width:318px;height:31px;background:var(--blue);color:#fff;font-size:10px;font-weight:600;text-align:center;line-height:31px}
.map{position:absolute;left:483px;top:56px;width:420px;height:237px;background:linear-gradient(135deg,#eef0ec,#e4e7ea 55%,#cfe4d3)}
.footer .brand-name{font-size:24px;color:#fff}
.footer p{font-size:13px;line-height:15.5px;color:#fff}
.flink{left:573px;font-size:17px;color:#fff;display:flex;align-items:center;gap:10px}
.fcontact{left:892px;font-size:15px;color:#fff;display:flex;align-items:center;gap:14px}
.fline{left:111px;top:3683px;width:1004px;height:1px;background:#545482}
.small{font-size:13px;color:#fff}
</style>
</head>
<body>
<div class="page">

  <header class="header">
    <div class="abs brand"><span class="mark"></span><span class="brand-name">Zerovan Medical</span></div>
    <div class="abs contact-chip" style="left:552px">
      <span class="ico"><svg width="24" height="24" viewBox="0 0 24 24"><path fill="#fff" d="M6.6 10.8a15 15 0 0 0 6.6 6.6l2.2-2.2c.3-.3.7-.4 1-.2 1.1.4 2.3.6 3.6.6.6 0 1 .4 1 1V20c0 .6-.4 1-1 1A17 17 0 0 1 3 4c0-.6.4-1 1-1h3.5c.6 0 1 .4 1 1 0 1.3.2 2.5.6 3.6.1.3 0 .7-.2 1z"/></svg></span>
      <div><b>Call Us</b><span>(+964) 750 000 4821</span></div>
    </div>
    <div class="abs contact-chip" style="left:873px">
      <span class="ico"><svg width="24" height="24" viewBox="0 0 24 24"><path fill="#fff" d="M3 6h18v12H3z"/><path d="M3 6l9 7 9-7" stroke="#1a9ad8" stroke-width="2" fill="none"/></svg></span>
      <div><b>Send an Email</b><span>hello@zerovanmedical.example</span></div>
    </div>
  </header>

  <nav class="abs nav">
    <a style="left:93px">Home</a>
    <a style="left:232px">About</a>
    <a style="left:373px">Services</a>
    <a style="left:548px">Projects</a>
    <a style="left:701px">Training</a>
    <a class="cta">Contact Us</a>
    <span class="soc" style="left:1008px"><svg width="10" height="10"><circle cx="5" cy="5" r="4" fill="#fff"/></svg></span>
    <span class="soc" style="left:1036px"><svg width="10" height="10"><circle cx="5" cy="5" r="4" fill="#fff"/></svg></span>
    <span class="soc" style="left:1064px"><svg width="10" height="10"><circle cx="5" cy="5" r="4" fill="#fff"/></svg></span>
  </nav>

  <section class="hero">
    <svg class="abs" style="left:0;top:145px" width="1200" height="650" viewBox="0 0 1200 650">
      <defs><linearGradient id="hg" x1="0" y1="0" x2="1" y2="0.3"><stop offset="0" stop-color="#2b8db3"/><stop offset=".5" stop-color="#7fc3d6"/><stop offset="1" stop-color="#f2f6f8"/></linearGradient></defs>
      <path d="M0 0H1200V540C1080 480 960 500 760 560 520 630 380 700 120 640 60 625 20 600 0 595Z" fill="url(#hg)"/>
      <path d="M0 540C60 620 170 660 300 640 460 615 560 560 760 540 940 522 1080 500 1200 560V600C1080 530 960 530 760 575 520 630 300 720 120 650 60 625 20 600 0 580Z" fill="#1a9ad8"/>
    </svg>
    <div class="abs hero-img" role="img" aria-label="Medical equipment: anesthesia workstation, surgical console and handpiece"></div>
    <h1 class="abs">Zerovan For<br>Medical Appliances</h1>
    <p class="abs">ZEROVAN MEDICAL Company is one of the specialized private companies in Iraq. Our job fields are lab. Diagnostics, equipment and medical appliances &amp; Ophthalmic Dept.</p>
    <a class="btn" style="left:77px;top:484px;width:145px;height:38px;line-height:38px;background:var(--navy)">Contact Us</a>
    <a class="btn" style="left:235px;top:484px;width:144px;height:38px;line-height:38px;background:var(--blue)">Our Projects</a>
  </section>

  <section class="about">
    <div class="abs about-img" role="img" aria-label="Operating room with C-arm imaging system and surgical lights"></div>
    <h2 class="abs">About Us</h2>
    <p class="abs">ZEROVAN MEDICAL Company is one of the specialized private companies in Iraq. Our job fields are lab. Diagnostics, equipment and medical appliances &amp; Ophthalmic Dept. ZEROVAN MEDICAL Established to be able cover all over Iraq not only Kurdistan Region because our business expanded to be able cover all over Iraq through our three offices in Baghdad , Basra &amp; Najaf cities.</p>
    <a class="btn" style="left:558px;top:1229px;width:167px;height:44px;line-height:44px;background:var(--navy);font-size:19px">Read More</a>
  </section>

  <section>
    <div class="abs services" role="img" aria-label="Faded hospital room backdrop in blue"></div>
    <h2 class="abs" style="left:0;width:1200px;top:1496px;text-align:center;font-size:46px;font-weight:600;color:#fff">Our Services</h2>
    <div class="abs svc-img" style="left:99px;background:radial-gradient(circle at 50% 45%,#f6f9fc,#d2e1ef 50%,#9fbfdc)" role="img" aria-label="Hospital imaging room equipment"></div>
    <div class="abs svc-img" style="left:462px;background:radial-gradient(circle at 55% 40%,#eef1f4,#b7c4cf 50%,#3a4a5c)" role="img" aria-label="Technician installing a surgical microscope"></div>
    <div class="abs svc-img" style="left:828px;background:radial-gradient(circle at 50% 50%,#f4f5f7,#d9dee3 55%,#b8c2cb)" role="img" aria-label="Patient monitor used in staff training"></div>
    <div class="abs svc-label" style="left:55px">Equipments</div>
    <div class="abs svc-label" style="left:418px">Installation</div>
    <div class="abs svc-label" style="left:784px">Training</div>
    <svg class="abs" style="left:36px;top:1740px" width="30" height="48"><path d="M25 4 6 24l19 20" stroke="#fff" stroke-width="4" fill="none"/></svg>
    <svg class="abs" style="left:1132px;top:1750px" width="30" height="48"><path d="M5 4l19 20L5 44" stroke="#fff" stroke-width="4" fill="none"/></svg>
  </section>

  <section class="partners">
    <div class="abs partner" style="left:55px"><i></i>Lumora</div>
    <div class="abs partner" style="left:335px"><i></i>Caldrex</div>
    <div class="abs partner" style="left:615px"><i></i>Vireo Lab</div>
    <div class="abs partner" style="left:895px;font-size:24px"><i></i>Brenwick</div>
  </section>

  <section class="projects">
    <h2 class="abs">Our Projects</h2>
    <div class="abs proj" style="left:99px"><div class="pic" style="background:radial-gradient(circle at 50% 40%,#f4f5f6,#c6ccd2 55%,#6f7880)" role="img" aria-label="Laparoscopy tower on cart"></div><p>30 complete units of Laparoscope distributed among 20 hospitals in Whole Iraq.</p><span class="go"><svg width="20" height="26"><path d="M5 3l10 10L5 23" stroke="#fff" stroke-width="3" fill="none"/></svg></span></div>
    <div class="abs proj active" style="left:467px"><div class="pic" style="background:radial-gradient(circle at 50% 60%,#f5f7f9,#c8d2dc 50%,#3d5278)" role="img" aria-label="Arthroscopy system in an operating room"></div><p>5 complete arthroscopy systems, supplied for 5 hospitals mostly in Baghdad.</p><span class="go"><svg width="20" height="26"><path d="M5 3l10 10L5 23" stroke="#fff" stroke-width="3" fill="none"/></svg></span></div>
    <div class="abs proj" style="left:825px"><div class="pic" style="background:radial-gradient(circle at 50% 45%,#f3f6f8,#d0dbe3 55%,#8ea2b2)" role="img" aria-label="Ceiling-mounted operating lights over a surgical table"></div><p>Full Automated Elisa System (Norvel Diagnostics co.)10 units.</p><span class="go"><svg width="20" height="26"><path d="M5 3l10 10L5 23" stroke="#fff" stroke-width="3" fill="none"/></svg></span></div>
    <svg class="abs" style="left:32px;top:2651px" width="30" height="48"><path d="M25 4 6 24l19 20" stroke="#1a9ad8" stroke-width="4" fill="none"/></svg>
    <svg class="abs" style="left:1128px;top:2661px" width="30" height="48"><path d="M5 4l19 20L5 44" stroke="#1a9ad8" stroke-width="4" fill="none"/></svg>
  </section>

  <div class="abs footer-band"></div>

  <section class="abs contact-box">
    <h3>Have Any Question?</h3>
    <div class="field" style="left:80px;top:104px;width:152px">Your Name</div>
    <div class="field" style="left:247px;top:104px;width:151px">Your Phone</div>
    <div class="field" style="left:80px;top:139px;width:152px">Email Address</div>
    <div class="field" style="left:247px;top:139px;width:151px">Select Service</div>
    <div class="field" style="left:80px;top:175px;width:318px;height:77px">Additional Message</div>
    <div class="send">GET IN TOUCH WITH US</div>
    <div class="map" role="img" aria-label="Street map of the office area in Erbil"></div>
  </section>

  <footer class="footer">
    <div class="abs" style="left:111px;top:3462px;display:flex;align-items:center;gap:10px"><span style="width:30px;height:30px;background:var(--blue);display:block"></span><span class="brand-name">Zerovan Medical</span></div>
    <p class="abs" style="left:111px;top:3540px;width:310px">ZEROVAN MEDICAL Company is one of the specialized private companies in Iraq. Our job fields are lab. Diagnostics, equipment and medical appliances &amp; Ophthalmic Dept.</p>
    <div class="abs flink" style="top:3465px"><svg width="10" height="14"><path d="M2 1l6 6-6 6" stroke="#1a9ad8" stroke-width="2" fill="none"/></svg>HOME</div>
    <div class="abs flink" style="top:3501px"><svg width="10" height="14"><path d="M2 1l6 6-6 6" stroke="#1a9ad8" stroke-width="2" fill="none"/></svg>ABOUT</div>
    <div class="abs flink" style="top:3537px"><svg width="10" height="14"><path d="M2 1l6 6-6 6" stroke="#1a9ad8" stroke-width="2" fill="none"/></svg>SERVICES</div>
    <div class="abs flink" style="top:3573px"><svg width="10" height="14"><path d="M2 1l6 6-6 6" stroke="#1a9ad8" stroke-width="2" fill="none"/></svg>PROJECTS</div>
    <div class="abs flink" style="top:3610px"><svg width="10" height="14"><path d="M2 1l6 6-6 6" stroke="#1a9ad8" stroke-width="2" fill="none"/></svg>CONTACT</div>
    <div class="abs fcontact" style="top:3478px"><svg width="20" height="20" viewBox="0 0 24 24"><path fill="#1a9ad8" d="M6.6 10.8a15 15 0 0 0 6.6 6.6l2.2-2.2c.3-.3.7-.4 1-.2 1.1.4 2.3.6 3.6.6.6 0 1 .4 1 1V20c0 .6-.4 1-1 1A17 17 0 0 1 3 4c0-.6.4-1 1-1h3.5c.6 0 1 .4 1 1 0 1.3.2 2.5.6 3.6.1.3 0 .7-.2 1z"/></svg>(+964) 750 000 4821</div>
    <div class="abs fcontact" style="top:3527px"><svg width="20" height="20" viewBox="0 0 24 24"><path fill="#1a9ad8" d="M2 7h20v13H2z"/><path d="M2 7l10 7 10-7" stroke="#1f1f5c" stroke-width="2" fill="none"/></svg>hello@zerovanmedical.example</div>
    <div class="abs fcontact" style="top:3575px"><svg width="20" height="22" viewBox="0 0 24 26"><path fill="#1a9ad8" d="M12 1a8 8 0 0 0-8 8c0 6 8 16 8 16s8-10 8-16a8 8 0 0 0-8-8z"/><circle cx="12" cy="9" r="3" fill="#1f1f5c"/></svg>Gulan Street No.14, Erbil</div>
    <div class="abs fline"></div>
    <div class="abs small" style="left:111px;top:3724px">Copyright 2024, All Rights Reserved.</div>
    <div class="abs small" style="left:882px;top:3724px">Privacy Policy | Term and Conditions</div>
  </footer>

</div>
</body>
</html>
```